business card for dental office

We need a business card design for an existing company follwing information we need on the card:
Tarvek L Osumbe, DDS
4526 Quillmere Court
Springfield, VA 22987
Ph: 703-555-0142 Fax:703-555-0187
www.grinvalemont.com info@grinvalemont.com
second side
Appointment
For
Date: day:
Time
if you are unable to keep your appointment, please contact us 24 hours in advance.
Note: Logo is attached to use with the card
Thanks
Industry/Entity Type
Dental Clinic
Contact Information for Business Card
Tarvek L Osumbe, DDS
4526 Quillmere Court
Springfield, VA 22987
second side
Appointment
For
Date: day:
Time
Thanks

```html
<!DOCTYPE html>
<html lang="en">
<head>
<meta charset="utf-8">
<title>Grinvalemont Dental Associates – Business Card</title>
<link rel="stylesheet" href="https://fonts.googleapis.com/css2?family=Open+Sans:wght@400;600&display=swap">
<style>
  :root {
    --backdrop: #3a3a3a;
    --card: #ffffff;
    --navy: #123a80;
    --sky: #1fb0e3;
    --ink: #1d1d1d;
    --rule: #333333;
  }
  * { box-sizing: border-box; margin: 0; padding: 0; }
  html, body { width: 1200px; height: 960px; overflow: hidden; }
  body {
    background: var(--backdrop);
    font-family: "Open Sans", Arial, sans-serif;
    position: relative;
  }
  .card {
    position: absolute;
    left: 320px;
    width: 560px;
    height: 320px;
    background: var(--card);
    overflow: hidden;
    box-shadow: 0 12px 30px rgba(0,0,0,.35);
  }
  .card--appointment { top: 100px; }
  .card--contact { top: 500px; }

  .brand {
    position: absolute;
    left: 26px;
    top: 22px;
    display: flex;
    align-items: center;
    gap: 8px;
    color: var(--navy);
    font-weight: 600;
    font-size: 15px;
    line-height: 1.15;
  }
  .brand__dot {
    width: 14px; height: 14px;
    border-radius: 50%;
    background: var(--sky);
    flex: none;
  }

  /* Appointment side */
  .appt__title {
    position: absolute;
    left: 0; right: 0; top: 92px;
    text-align: center;
    color: var(--navy);
    font-size: 19px;
  }
  .field {
    position: absolute;
    display: flex;
    align-items: flex-end;
    font-size: 14px;
    color: var(--ink);
  }
  .field__line {
    flex: 1;
    border-bottom: 1px solid var(--rule);
    margin-left: 6px;
    height: 16px;
  }
  .field--for  { left: 26px; top: 128px; width: 508px; }
  .field--date { left: 26px; top: 170px; width: 160px; }
  .field--day  { left: 200px; top: 170px; width: 170px; }
  .field--time { left: 384px; top: 170px; width: 150px; }
  .appt__note {
    position: absolute;
    left: 26px; top: 212px;
    width: 380px;
    font-size: 12.5px;
    line-height: 1.45;
    color: var(--ink);
  }

  .tools {
    position: absolute;
    right: 26px;
    width: 86px;
    height: 66px;
    background: var(--sky);
    border-radius: 4px 4px 0 0;
  }
  .card--appointment .tools { bottom: 0; }
  .card--contact .tools { bottom: 66px; height: 60px; }

  /* Contact side */
  .contact__name {
    position: absolute;
    right: 30px; top: 96px;
    font-size: 24px;
    color: var(--navy);
  }
  .contact__name span { color: var(--sky); }
  .contact__list {
    position: absolute;
    left: 26px; top: 148px;
    list-style: none;
    font-size: 13.5px;
    color: var(--navy);
    line-height: 1.35;
  }
  .contact__list li { display: flex; gap: 10px; margin-bottom: 6px; }
  .contact__list svg { flex: none; margin-top: 2px; }
  .contact__web { color: var(--ink); }
  .band {
    position: absolute;
    left: 0; right: 0; bottom: 0;
    height: 66px;
    background: var(--sky);
    color: #ffffff;
    font-size: 14px;
    display: flex;
    align-items: center;
    padding-left: 26px;
    gap: 14px;
  }
  .band__divider { width: 1px; height: 18px; background: #ffffff; }
</style>
</head>
<body>

<section class="card card--appointment">
  <div class="brand">
    <span class="brand__dot"></span>
    <span>Grinvalemont Dental<br>Associates</span>
  </div>
  <h2 class="appt__title">Appointment</h2>
  <div class="field field--for">For:<span class="field__line"></span></div>
  <div class="field field--date">Date:<span class="field__line"></span></div>
  <div class="field field--day">Day:<span class="field__line"></span></div>
  <div class="field field--time">Time:<span class="field__line"></span></div>
  <p class="appt__note">If you are unable to keep your appointment,<br>please contact us 24 hours in advance.</p>
  <div class="tools" role="img" aria-label="Row of dental instrument silhouettes"></div>
</section>

<section class="card card--contact">
  <div class="brand">
    <span class="brand__dot"></span>
    <span>Grinvalemont Dental<br>Associates</span>
  </div>
  <h1 class="contact__name">Tarvek L Osumbe, <span>DDS</span></h1>
  <ul class="contact__list">
    <li>
      <svg width="14" height="14" viewBox="0 0 14 14" aria-hidden="true"><path d="M7 1 L13 7 H11 V13 H8.5 V9 H5.5 V13 H3 V7 H1 Z" fill="var(--sky)"/></svg>
      <span>4526 Quillmere Court<br>Springfield, VA 22987</span>
    </li>
    <li>
      <svg width="14" height="30" viewBox="0 0 14 30" aria-hidden="true">
        <circle cx="7" cy="7" r="5.5" fill="none" stroke="var(--sky)" stroke-width="1.5"/>
        <path d="M1.5 7 H12.5 M7 1.5 C4 4 4 10 7 12.5 M7 1.5 C10 4 10 10 7 12.5" fill="none" stroke="var(--sky)" stroke-width="1"/>
        <rect x="1" y="19" width="12" height="8" fill="var(--sky)"/>
        <path d="M1 19 L7 24 L13 19" fill="none" stroke="#fff" stroke-width="1"/>
      </svg>
      <span class="contact__web">www.grinvalemont.com<br>info@grinvalemont.com</span>
    </li>
  </ul>
  <div class="tools" role="img" aria-label="Row of dental instrument silhouettes"></div>
  <div class="band">
    <span>Ph: 703-555-0142</span>
    <span class="band__divider"></span>
    <span>Fax: 703-555-0187</span>
  </div>
</section>

</body>
</html>
```